Brand-new Pediatric Dental Practice needs a website

We are a brand-new dental practice that will specialize in treating children. We want a gorgeous and easily navigable dental practice website that would make a good first impression to potential patients and their parents. It should be modern, SEO-friendly, mobile responsive, and optimized to win new patients.

Target Market(s)

Parents

Industry/Entity Type

Healthcare/Dentistry

Coding

Coded - Design and coding required

Number of Pages Required

4 page

Requirements
Must have
• Use the Wix website building platform. 4 pages: home, meet our dentists, services, contact us
Nice to have
• has a link to our facebook, instagram

```html
<!DOCTYPE html>
<html lang="en">
<head>
<meta charset="utf-8">
<title>Maple Grove Kids Dental</title>
<link href="https://fonts.googleapis.com/css2?family=Roboto:wght@400;500;700&family=Rubik:wght@500;700&display=swap" rel="stylesheet">
<style>
:root{
  --dark:#3a3a3c;
  --field:#4a4a4d;
  --green:#2f9e58;
  --green-light:#5cbf7b;
  --bg:#f5f5f5;
  --white:#ffffff;
  --ink:#2f2f2f;
  --muted:#6b6b6b;
}
*{box-sizing:border-box;margin:0;padding:0}
html,body{width:1200px;height:2985px;overflow:hidden;background:var(--bg)}
body{font-family:"Roboto",sans-serif;color:var(--ink);position:relative}
.abs{position:absolute}
.topbar{left:0;top:0;width:1200px;height:86px;background:var(--dark)}
.brand{left:112px;top:22px;display:flex;align-items:center;gap:10px;color:var(--white);font-weight:500;font-size:19px}
.brand-dot{width:34px;height:34px;border-radius:50%;background:var(--green-light)}
.phone-box{left:877px;top:0;width:323px;height:86px;background:var(--green);display:flex;align-items:center;justify-content:center;gap:14px;color:var(--white);font-weight:500;font-size:22px}
.nav{left:0;top:86px;width:1200px;height:67px;background:var(--bg)}
.nav a{position:absolute;top:27px;font-size:15px;font-weight:500;color:var(--ink);text-decoration:none}
.nav a.active{color:var(--green)}
.login{display:flex;align-items:center;gap:10px}
.hero-photo{left:0;top:153px;width:892px;height:531px;background:
  radial-gradient(ellipse 150px 240px at 110px 430px,#7fcfc4 0%,rgba(127,207,196,0) 100%),
  radial-gradient(ellipse 190px 260px at 380px 330px,#1f8fa8 0%,rgba(31,143,168,.6) 45%,rgba(31,143,168,0) 100%),
  radial-gradient(ellipse 120px 150px at 250px 330px,#e7c3ad 0%,rgba(231,195,173,0) 100%),
  radial-gradient(ellipse 140px 110px at 320px 120px,#d9b39e 0%,rgba(217,179,158,0) 100%),
  radial-gradient(ellipse 260px 200px at 680px 160px,#ffffff 0%,rgba(255,255,255,0) 100%),
  radial-gradient(ellipse 200px 140px at 400px 470px,#f4f1ef 0%,rgba(244,241,239,0) 100%),
  linear-gradient(120deg,#d9e2e1 0%,#eef1f0 45%,#c9d2d1 75%,#e4e8e8 100%)}
.hero-card{left:660px;top:310px;width:429px;height:219px;background:var(--white);padding:38px 35px}
.hero-card h1{font-family:"Rubik",sans-serif;font-weight:700;font-size:36px;line-height:51px;color:var(--ink);letter-spacing:.5px}
.btn{display:flex;color:var(--white);font-weight:700;font-size:15px;text-transform:uppercase}
.btn .label{background:var(--green-light);display:flex;align-items:center;justify-content:center}
.btn .arrow{background:var(--green);display:flex;align-items:center;justify-content:center}
.hero-btn{left:890px;top:478px;height:51px}
.hero-btn .label{width:147px}.hero-btn .arrow{width:52px}
.card{width:283px;height:282px;background:var(--white);box-shadow:0 2px 6px rgba(0,0,0,.06)}
.card .photo{height:197px}
.card h3{font-size:16px;font-weight:500;text-align:center;line-height:85px;color:var(--ink)}
.p1{background:radial-gradient(ellipse 60px 80px at 125px 120px,#f2a33a,rgba(242,163,58,0)),radial-gradient(ellipse 60px 110px at 215px 110px,#f2f5f7,rgba(242,245,247,0)),radial-gradient(ellipse 50px 90px at 35px 130px,#5c8fb8,rgba(92,143,184,0)),linear-gradient(135deg,#b9cfdc,#dfe7ec 60%,#c4d2da)}
.p2{background:radial-gradient(ellipse 70px 110px at 70px 110px,#eef1f3,rgba(238,241,243,0)),radial-gradient(ellipse 60px 100px at 180px 120px,#e7b7b5,rgba(231,183,181,0)),radial-gradient(ellipse 40px 70px at 175px 60px,#3b2b28,rgba(59,43,40,0)),linear-gradient(135deg,#d6dde2,#c9d1d8 60%,#e3e7ea)}
.p3{background:radial-gradient(ellipse 70px 120px at 225px 120px,#2f4f78,rgba(47,79,120,0)),radial-gradient(ellipse 60px 70px at 60px 130px,#3e4a63,rgba(62,74,99,0)),radial-gradient(ellipse 40px 30px at 80px 70px,#9ed76a,rgba(158,215,106,0)),linear-gradient(135deg,#dfe5e3,#c7d2d6 60%,#d8dee0)}
.p4{background:radial-gradient(ellipse 80px 100px at 150px 80px,#f0cdb5,rgba(240,205,181,0)),radial-gradient(ellipse 100px 60px at 160px 170px,#8fc9dc,rgba(143,201,220,0)),radial-gradient(ellipse 60px 100px at 240px 90px,#c87d4e,rgba(200,125,78,0)),linear-gradient(135deg,#2b4f83,#3f73b0 50%,#9ac7da)}
.p5{background:radial-gradient(ellipse 80px 100px at 90px 90px,#f4f6f7,rgba(244,246,247,0)),radial-gradient(ellipse 80px 60px at 210px 170px,#8fd0dc,rgba(143,208,220,0)),radial-gradient(ellipse 50px 70px at 220px 60px,#c98f63,rgba(201,143,99,0)),linear-gradient(135deg,#e8eef2,#d4dde3 60%,#c6d6dc)}
.p6{background:radial-gradient(ellipse 60px 60px at 40px 150px,#4d9b6a,rgba(77,155,106,0)),radial-gradient(ellipse 50px 60px at 60px 90px,#3a5f9e,rgba(58,95,158,0)),radial-gradient(ellipse 70px 110px at 220px 110px,#f5f7f9,rgba(245,247,249,0)),linear-gradient(135deg,#e7eef1,#dfe6ea 50%,#cdd8de)}
.view-btn{left:516px;top:1415px;height:50px}
.view-btn .label{width:117px}.view-btn .arrow{width:51px}
.about{left:111px;top:1546px;width:978px;height:472px;background:var(--white);box-shadow:0 2px 8px rgba(0,0,0,.05)}
.about-text{left:47px;top:80px;width:397px}
.about h2{font-family:"Rubik",sans-serif;font-weight:700;font-size:29px;margin-bottom:30px}
.about p{font-size:14px;line-height:26px;color:var(--muted);text-align:justify;margin-bottom:15px}
.about-photo{left:488px;top:0;width:490px;height:472px;background:
  radial-gradient(ellipse 190px 170px at 150px 190px,#6fb6dc 0%,rgba(111,182,220,0) 100%),
  radial-gradient(ellipse 110px 100px at 110px 70px,#6b4a34 0%,rgba(107,74,52,0) 100%),
  radial-gradient(ellipse 120px 130px at 400px 290px,#e8b79a 0%,rgba(232,183,154,0) 100%),
  radial-gradient(ellipse 90px 70px at 230px 300px,#f3f4f5 0%,rgba(243,244,245,0) 100%),
  radial-gradient(ellipse 260px 100px at 260px 440px,#5278a6 0%,rgba(82,120,166,0) 100%),
  linear-gradient(135deg,#d7dfe4,#eef1f3 45%,#dfe5e8)}
.reviews{left:0;top:2095px;width:1200px;text-align:center}
.reviews h2{font-family:"Rubik",sans-serif;font-weight:700;font-size:29px}
.reviews p{width:760px;margin:32px auto 0;font-size:14px;line-height:27px;color:var(--muted)}
.reviewer{margin-top:22px;font-size:17px;color:var(--green)}
.reviewer b{font-weight:500}
.country{margin-top:6px;font-size:15px;font-weight:500;color:var(--ink)}
.chev{top:2185px}
.footer{left:0;top:2410px;width:1200px;height:575px;background:var(--dark)}
.chat{left:1003px;top:2386px;width:171px;height:49px;background:var(--green);border-radius:4px;display:flex;align-items:center;justify-content:center;gap:12px;color:var(--white);font-weight:700;font-size:18px}
.contact-title{left:0;top:2460px;width:1200px;text-align:center;color:var(--white);font-family:"Rubik",sans-serif;font-weight:700;font-size:37px}
.field{left:258px;width:684px;background:var(--field);color:#e6e6e6;font-size:14px;padding:14px 18px}
.send{left:258px;top:2786px;width:684px;height:46px;background:var(--green);color:var(--white);font-weight:700;font-size:14px;display:flex;align-items:center;justify-content:center}
.social{left:110px;top:2905px;display:flex;gap:22px}
.social span{width:22px;height:22px;border-radius:50%;background:var(--white)}
.divider{top:2878px;width:1px;height:76px;background:#bbb}
.info{color:var(--white);font-size:15px;line-height:24px}
.info-row{display:flex;gap:14px;align-items:flex-start}
</style>
</head>
<body>

<header class="abs topbar"></header>
<div class="abs brand"><span class="brand-dot"></span>Maple Grove</div>
<div class="abs phone-box">
  <svg width="18" height="18" viewBox="0 0 24 24"><path fill="#fff" d="M6.6 10.8a15 15 0 0 0 6.6 6.6l2.2-2.2a1 1 0 0 1 1-.25 11.4 11.4 0 0 0 3.6.57 1 1 0 0 1 1 1V20a1 1 0 0 1-1 1A17 17 0 0 1 3 4a1 1 0 0 1 1-1h3.5a1 1 0 0 1 1 1c0 1.250.2 2.45.57 3.57a1 1 0 0 1-.25 1z"/></svg>
  +1 (555) 014 2736
</div>

<nav class="abs nav">
  <a class="active" style="left:110px" href="#">HOME</a>
  <a style="left:193px" href="#">MEET OUR DENTISTS</a>
  <a style="left:381px" href="#">SERVICES</a>
  <a style="left:491px" href="#">CONTACT US</a>
  <a class="login" style="left:821px" href="#">
    <svg width="16" height="16" viewBox="0 0 24 24"><circle cx="12" cy="12" r="10" fill="none" stroke="#2f9e58" stroke-width="2"/><circle cx="12" cy="10" r="3.5" fill="#2f9e58"/><path d="M5.5 18.5c2-3 11-3 13 0" fill="#2f9e58"/></svg>LOGIN</a>
</nav>

<div class="abs hero-photo" role="img" aria-label="Dentist in a mask examining a young girl in a dental chair"></div>
<div class="abs hero-card"><h1>PEDIATRIC DENTAL<br>PRACTISE</h1></div>
<a class="abs btn hero-btn"><span class="label">Get Started</span><span class="arrow"><svg width="12" height="16" viewBox="0 0 12 16"><path d="M3 2l6 6-6 6" stroke="#fff" stroke-width="2" fill="none"/></svg></span></a>

<section>
  <div class="abs card" style="left:154px;top:775px"><div class="photo p1" role="img" aria-label="Child smiling during a dental check-up"></div><h3>PEDIATRIC DENTAL</h3></div>
  <div class="abs card" style="left:458px;top:775px"><div class="photo p2" role="img" aria-label="Dentist consulting with a teenage patient"></div><h3>PEDIATRIC DENTAL</h3></div>
  <div class="abs card" style="left:763px;top:775px"><div class="photo p3" role="img" aria-label="Dentist giving a high five to a young patient"></div><h3>PEDIATRIC DENTAL</h3></div>
  <div class="abs card" style="left:154px;top:1082px"><div class="photo p4" role="img" aria-label="Girl having her teeth examined"></div><h3>PEDIATRIC DENTAL</h3></div>
  <div class="abs card" style="left:458px;top:1082px"><div class="photo p5" role="img" aria-label="Dentist showing instruments to a girl"></div><h3>PEDIATRIC DENTAL</h3></div>
  <div class="abs card" style="left:763px;top:1082px"><div class="photo p6" role="img" aria-label="Boy in a dental chair with dentist"></div><h3>PEDIATRIC DENTAL</h3></div>
</section>
<a class="abs btn view-btn"><span class="label">View All</span><span class="arrow"><svg width="12" height="16" viewBox="0 0 12 16"><path d="M3 2l6 6-6 6" stroke="#fff" stroke-width="2" fill="none"/></svg></span></a>

<section class="abs about">
  <div class="abs about-text">
    <h2>ABOUT US</h2>
    <p>Lorem ipsum dolor sit amet, consectetur adipiscing elit, sed do eiusmod tempor incididunt ut labore et dolore magna aliqua. Ut enim ad minim veniam, quis nostrud exercitation ullamco laboris nisi ut aliquip exduis aute irure dolor in repreh enderit in voluptate velit esse cillum doloreea.</p>
    <p>Commodo consequat duis aute irure dolor in reprehenderit in voluptate velit esse cillum dolore eu fugiat nulla pariatur. Excepteur sint occaecat cupidatat non proident, sunt in culpa qui officia deserunt mollit anim id est laborumea.</p>
  </div>
  <div class="abs about-photo" role="img" aria-label="Dentist examining a smiling girl's teeth"></div>
</section>

<section class="abs reviews">
  <h2>OUR HAPPY CUSTOMERS</h2>
  <p>Lorem ipsum dolor sit amet, consectetur adipiscing elit, sed do eiusmod tempor incididunt ut labore et dolore magna aliqua. Ut enim ad minim veniam, quis nostrud exercitation ullamco laboris nisi ut aliquip ex ea commodo consequat duis aute irure dolor in reprehenderit in voluptate velit esse cillum dolorea.</p>
  <div class="reviewer"><b>Hannah Reed,</b> NYC</div>
  <div class="country">United States</div>
</section>
<svg class="abs chev" style="left:110px" width="16" height="28" viewBox="0 0 16 28"><path d="M13 2L3 14l10 12" stroke="#999" stroke-width="2.5" fill="none"/></svg>
<svg class="abs chev" style="left:1073px" width="16" height="28" viewBox="0 0 16 28"><path d="M3 2l10 12L3 26" stroke="#333" stroke-width="2.5" fill="none"/></svg>

<footer class="abs footer"></footer>
<div class="abs chat">
  <svg width="20" height="20" viewBox="0 0 24 24"><circle cx="12" cy="12" r="10" fill="none" stroke="#fff" stroke-width="2"/><circle cx="12" cy="10" r="3.5" fill="#fff"/><path d="M5.5 18.5c2-3 11-3 13 0" fill="#fff"/></svg>Let’s Chat!
</div>
<h2 class="abs contact-title">CONTACT US</h2>
<div class="abs field" style="top:2533px;height:47px">Name</div>
<div class="abs field" style="top:2587px;height:47px">Email</div>
<div class="abs field" style="top:2640px;height:47px">Phone</div>
<div class="abs field" style="top:2693px;height:85px">Message</div>
<div class="abs send">SEND MESSAGE</div>

<div class="abs social" aria-label="Social media links"><span></span><span></span><span></span></div>
<div class="abs divider" style="left:278px"></div>
<div class="abs info info-row" style="left:333px;top:2894px">
  <svg width="12" height="16" viewBox="0 0 12 16" style="margin-top:4px"><path d="M6 0a6 6 0 0 0-6 6c0 4.5 6 10 6 10s6-5.5 6-10a6 6 0 0 0-6-6zm0 8.5A2.5 2.5 0 1 1 6 3.5a2.5 2.5 0 0 1 0 5z" fill="#2f9e58"/></svg>
  <div>465, Lorum Ipsum Dolore<br>United States</div>
</div>
<div class="abs divider" style="left:600px"></div>
<div class="abs info" style="left:671px;top:2892px">
  <div class="info-row"><svg width="14" height="14" viewBox="0 0 24 24" style="margin-top:4px"><path fill="#2f9e58" d="M6.6 10.8a15 15 0 0 0 6.6 6.6l2.2-2.2a1 1 0 0 1 1-.25 11.4 11.4 0 0 0 3.6.57 1 1 0 0 1 1 1V20a1 1 0 0 1-1 1A17 17 0 0 1 3 4a1 1 0 0 1 1-1h3.5a1 1 0 0 1 1 1c0 1.25.2 2.45.57 3.57a1 1 0 0 1-.25 1z"/></svg>+1 (555) 014 2736</div>
  <div class="info-row" style="margin-top:4px"><svg width="14" height="14" viewBox="0 0 24 24" style="margin-top:5px"><rect x="1" y="4" width="22" height="16" rx="2" fill="#2f9e58"/><path d="M2 5l10 8 10-8" stroke="#3a3a3c" stroke-width="2" fill="none"/></svg>hello@maplegrovekids.com</div>
</div>
<div class="abs divider" style="left:891px"></div>
<div class="abs info" style="left:952px;top:2893px">© 2022 by Pediatric<br>Dental Practise</div>

</body>
</html>
```